Stationary Set Rebrand for Brenton

We are a Canadian Distribution and Service Company that was established in 1969. Over the past 5 decades we have expanded our business and have warehouses across Canada. We specialize in adhesive tapes, adhesives, films, safety, warehouse, shipping, janitorial and packaging supplies.

We have updated our logo design and would like a new corporate branding identity that includes a new fresh Stationary Set (Business Cards, Letterhead, Letterhead MS Word, Envelope, Presentation Folders, Email Signatures, Notepad Covers, etc.)

Target Market(s)

Industrial Business Sector

Font styles to use
Sans Serif

Colors
0054AA
0677BA
7BADD7
CADEEF
E8F1F8
0094D4
00A9DD
6FCCEA
C7EBF8
E9F6FB
00AB8E
00BBA5
67D7C9
C6EFE9
E9F9F6
EB3D1F
EC4F4E
F09395
F8D3D4
FCEDEE

Requirements
Should not have
• Colors not too light, darker colours preferred

```html
<!DOCTYPE html>
<html lang="en">
<head>
<meta charset="utf-8">
<title>Brenton Stationery Set</title>
<link rel="stylesheet" href="https://fonts.googleapis.com/css2?family=Lato:wght@400;700;900&display=swap">
<style>
:root{
  --ink:#1a1a1a;
  --grey-text:#555555;
  --red:#d20a11;
  --paper:#ffffff;
  --bg-left:#e8e8e8;
  --bg-right:#dedede;
  --divider:#ffffff;
  --dieline:#8a8a8a;
  --card-back:#2b2b2b;
}
*{margin:0;padding:0;box-sizing:border-box}
html,body{width:1200px;height:877px;overflow:hidden}
body{position:relative;background:var(--divider);font-family:'Lato',sans-serif;color:var(--ink)}
.panel{position:absolute;overflow:hidden}
.panel--cards{left:0;top:0;width:604px;height:400px;background:var(--bg-left)}
.panel--letterhead{left:0;top:403px;width:604px;height:474px;background:var(--bg-left)}
.panel--envelope{left:607px;top:0;width:593px;height:485px;background:var(--bg-right)}
.panel--card-flat{left:607px;top:489px;width:593px;height:388px;background:var(--bg-right)}

.wordmark{display:block;font-weight:900;color:var(--ink);line-height:1;letter-spacing:-0.5px;white-space:nowrap}
.tagline{display:block;font-weight:700;color:var(--ink);line-height:1;white-space:nowrap}
.accent-disc{position:absolute;border-radius:50%;background:var(--red)}
.address{white-space:nowrap}
.contact{list-style:none;white-space:nowrap}
.contact li{display:flex;align-items:center;gap:5px;color:var(--grey-text)}
.icon{flex:none;background:var(--ink);border-radius:1px;position:relative}
.icon::after{content:"";position:absolute;left:50%;top:50%;width:50%;height:50%;transform:translate(-50%,-50%);border-radius:50%;background:var(--red)}

/* business card front */
.card{position:absolute;width:407px;height:163px;background:var(--paper);overflow:hidden}
.card .wordmark{position:absolute;left:22px;top:20px;font-size:36px}
.card .tagline{position:absolute;left:22px;top:55px;font-size:8px}
.card .person{position:absolute;left:22px;top:74px}
.card .person-name{font-weight:700;font-size:16px;line-height:1.1}
.card .person-role{font-size:10px;color:var(--grey-text)}
.card .address{position:absolute;left:22px;top:118px;font-size:8.5px;line-height:11px;color:var(--grey-text)}
.card .contact{position:absolute;left:141px;top:115px;font-size:8.5px;line-height:11px}
.card .icon{width:8px;height:8px}
.card .accent-disc{left:257px;top:12px;width:140px;height:140px}

.card-small{position:absolute;transform:scale(0.64);transform-origin:top left}
.card-back{position:absolute;left:40px;top:140px;width:260px;height:104px;background:var(--card-back);display:flex;flex-direction:column;align-items:center;justify-content:center}
.card-back .wordmark{color:var(--paper);font-size:24px}
.card-back .tagline{color:var(--paper);font-size:6px;margin-top:3px}

/* letterhead */
.letterhead{position:absolute;left:147px;top:18px;width:311px;height:440px;background:var(--paper)}
.letterhead .wordmark{position:absolute;left:24px;top:26px;font-size:28px}
.letterhead .tagline{position:absolute;left:24px;top:57px;font-size:7px}
.letterhead .accent-disc{left:196px;top:232px;width:90px;height:90px}
.letterhead .address{position:absolute;left:140px;top:396px;font-size:6px;line-height:8px;color:var(--grey-text)}
.letterhead .contact{position:absolute;left:218px;top:394px;font-size:6px;line-height:8px}
.letterhead .icon{width:6px;height:6px}

/* envelope */
.envelope-dieline{position:absolute;left:0;top:0}
.envelope-face{position:absolute;left:0;top:0;width:593px;height:485px}
.envelope-face .wordmark{position:absolute;left:79px;top:104px;font-size:34px}
.envelope-face .tagline{position:absolute;left:80px;top:136px;font-size:7.5px}
.envelope-face .address{position:absolute;left:83px;top:232px;font-size:6px;line-height:8px;color:var(--grey-text)}
.envelope-face .contact{position:absolute;left:81px;top:260px;font-size:6px;line-height:10px}
.envelope-face .icon{width:7px;height:7px}
</style>
</head>
<body>

<section class="panel panel--cards">
  <div class="card-back">
    <span class="wordmark">Brenton</span>
    <span class="tagline">Tape and Packaging Specialists</span>
  </div>
  <div class="card-small" style="left:315px;top:140px">
    <div class="card">
      <span class="wordmark">Brenton</span>
      <span class="tagline">Tape and Packaging Specialists</span>
      <div class="person"><p class="person-name">Halden</p><p class="person-role">Chief Executive</p></div>
      <p class="address">Brenton Sales ON Ltd.<br>27-512 Cedar Ridge Rd<br>Guelph, ON N1K 2T4</p>
      <ul class="contact">
        <li><span class="icon"></span>(555) 201-3390</li>
        <li><span class="icon"></span>info@brentonsales.com</li>
        <li><span class="icon"></span>on.brentonsales.com</li>
      </ul>
      <span class="accent-disc"></span>
    </div>
  </div>
</section>

<section class="panel panel--letterhead">
  <div class="letterhead">
    <span class="wordmark">Brenton</span>
    <span class="tagline">Tape and Packaging Specialists</span>
    <span class="accent-disc"></span>
    <p class="address">Brenton Sales ON Ltd.<br>27-512 Cedar Ridge Rd<br>Guelph, ON N1K 2T4</p>
    <ul class="contact">
      <li><span class="icon"></span>(555) 201-3390</li>
      <li><span class="icon"></span>info@brentonsales.com</li>
      <li><span class="icon"></span>on.brentonsales.com</li>
    </ul>
  </div>
</section>

<section class="panel panel--envelope">
  <svg class="envelope-dieline" width="593" height="485" viewBox="0 0 593 485">
    <defs><clipPath id="envelope-body"><rect x="65" y="93" width="431" height="204"/></clipPath></defs>
    <path d="M65 93 L36 113 Q36 118 36 120 L36 268 Q36 278 60 290 L65 297 Z" fill="#fff" stroke="var(--dieline)" stroke-width="0.8"/>
    <path d="M496 93 L525 113 Q525 118 525 120 L525 268 Q525 278 501 290 L496 297 Z" fill="#fff" stroke="var(--dieline)" stroke-width="0.8"/>
    <path d="M65 297 L70 305 L70 466 Q70 473 77 473 L484 473 Q491 473 491 466 L491 305 L496 297 Z" fill="#fff" stroke="var(--dieline)" stroke-width="0.8"/>
    <path d="M65 93 L80 43 Q83 36 92 36 L470 36 Q479 36 482 43 L496 93 Z" fill="#0d0d0d"/>
    <circle cx="281" cy="63" r="15" fill="var(--red)"/>
    <rect x="65" y="93" width="431" height="204" fill="#fff" stroke="var(--dieline)" stroke-width="0.8"/>
    <circle cx="438" cy="232" r="62" fill="var(--red)" clip-path="url(#envelope-body)"/>
  </svg>
  <div class="envelope-face">
    <span class="wordmark">Brenton</span>
    <span class="tagline">Tape and Packaging Specialists</span>
    <p class="address">Brenton Sales ON Ltd.<br>27-512 Cedar Ridge Rd<br>Guelph, ON N1K 2T4</p>
    <ul class="contact">
      <li><span class="icon"></span>(555) 201-3390</li>
      <li><span class="icon"></span>info@brentonsales.com</li>
      <li><span class="icon"></span>on.brentonsales.com</li>
    </ul>
  </div>
</section>

<section class="panel panel--card-flat">
  <div class="card" style="left:74px;top:108px">
    <span class="wordmark">Brenton</span>
    <span class="tagline">Tape and Packaging Specialists</span>
    <div class="person"><p class="person-name">Halden</p><p class="person-role">Chief Executive</p></div>
    <p class="address">Brenton Sales ON Ltd.<br>27-512 Cedar Ridge Rd<br>Guelph, ON N1K 2T4</p>
    <ul class="contact">
      <li><span class="icon"></span>(555) 201-3390</li>
      <li><span class="icon"></span>info@brentonsales.com</li>
      <li><span class="icon"></span>on.brentonsales.com</li>
    </ul>
    <span class="accent-disc"></span>
  </div>
</section>

</body>
</html>
```